依頼詳細
ラフ案を添付致しますのでそちらをベースにブラッシュアップお願いいたします。

お水の特徴は以下となります。
①分子が細かい(水分子のナノコロイダル化、六角形構造)
②浸透力が高い(脳細胞まで届くイメージ)
③科学的に研究された機能のある水

全体デザインは、上記イメージを踏まえてエネルギー溢れるようなデザインを希望致します。
記載項目
下部に記載する社名等はデザイン選定後にお伝えさせていただきます。
サイズ
A4
ページ数
片面
希望イメージ
シンプル 複雑
単色 カラフル
暗い 明るい
日常 高級
遊び心 厳粛
未来的 伝統的
女性的 男性的
希望する色
水色系
納品ファイル
• 高解像度JPG (.jpg)
• イラストレーター形式 (.ai)
• PNG形式 (.png)
補足説明
■ 選んだ理由

インパクトと躍動感のあるデザインだった為選ばせて頂きました。

■ 提案者全員のお礼・コメント

この度はたくさんのご提案誠にありがとうございます。
素敵なデザインが多く選定に悩ませて頂きました。
また機会がありましたらその際はどうぞよろしくお願い致します。

```html
<!DOCTYPE html>
<html lang="ja">
<head>
<meta charset="UTF-8">
<title>高濃度シリカ水</title>
<link href="https://fonts.googleapis.com/css2?family=Noto+Serif+JP:wght@500;700&family=Noto+Sans+JP:wght@400;500;700&display=swap" rel="stylesheet">
<style>
:root{
  --sky:#dff1fb;
  --sky-deep:#a9d8f1;
  --blue:#2f7fc1;
  --blue-dark:#1e5e98;
  --ink:#3a4a58;
  --gold-a:#fff8d6;
  --gold-b:#f4d36a;
  --white:#ffffff;
  --accent:#2c9be0;
}
*{margin:0;padding:0;box-sizing:border-box}
html,body{width:849px;height:1200px;overflow:hidden}
body{font-family:"Noto Sans JP",sans-serif;color:var(--ink);background:var(--white)}
.page{position:relative;width:849px;height:1200px;overflow:hidden;
  background:linear-gradient(180deg,var(--sky) 0%,#eef8fd 40%,var(--sky-deep) 62%,#f3fafe 78%,var(--white) 100%)}
.lead{position:absolute;top:34px;width:100%;text-align:center;font-family:"Noto Serif JP",serif;font-weight:500;font-size:23px;color:var(--ink);letter-spacing:.06em}
.title{position:absolute;top:70px;width:100%;text-align:center;font-family:"Noto Serif JP",serif;font-weight:700;font-size:66px;color:var(--blue);letter-spacing:.06em}
.lot{position:absolute;top:176px;left:50%;transform:translateX(-50%);font-family:"Noto Serif JP",serif;font-size:21px;color:var(--blue);padding:2px 24px;border-bottom:1.5px solid var(--blue)}
.bottles{position:absolute;left:40px;top:220px;width:400px;height:470px;border-radius:40% 60% 45% 55%;
  background:radial-gradient(ellipse at 45% 45%,#ffffff 0%,#cfeaf8 45%,rgba(150,205,235,.5) 70%,rgba(255,255,255,0) 100%)}
.feature{position:absolute;border-radius:50%;display:flex;align-items:center;justify-content:center;text-align:center;
  background:radial-gradient(circle at 40% 35%,var(--gold-a) 0%,#fbe8a4 55%,var(--gold-b) 100%);
  box-shadow:0 0 18px rgba(244,211,106,.55);font-family:"Noto Serif JP",serif;font-weight:500;color:var(--ink);line-height:1.45}
.f1{left:636px;top:226px;width:114px;height:114px;font-size:17px}
.f2{left:540px;top:314px;width:108px;height:108px;font-size:17px}
.f3{left:606px;top:422px;width:146px;height:146px;font-size:15px}
.f4{left:425px;top:566px;width:84px;height:84px;font-size:15px}
.intro{position:absolute;top:708px;width:100%;text-align:center;font-size:16px;line-height:1.85;color:var(--ink);letter-spacing:.03em}
.card{position:absolute;top:818px;height:310px;background:rgba(255,255,255,.85);border:1px solid #cfe3f0}
.card-silica{left:212px;width:206px;padding:14px 12px}
.card-water{left:438px;width:206px;padding:12px 12px}
.card-head{text-align:center;font-family:"Noto Serif JP",serif;color:var(--ink);border-bottom:1px solid #bcd4e4;padding-bottom:8px;margin-bottom:12px}
.card-head .main{font-size:16px;font-weight:700}
.card-head .sub{font-size:11px}
.points{list-style:none;font-size:11.5px;line-height:1.6}
.points li{display:flex;gap:6px;margin-bottom:14px}
.points li::before{content:"";flex:0 0 9px;height:9px;margin-top:5px;background:var(--accent)}
.card-water .tag{text-align:center;font-size:11px;color:var(--ink)}
.card-water .name{background:var(--accent);color:var(--white);text-align:center;font-family:"Noto Serif JP",serif;font-size:20px;font-weight:700;padding:2px 0;margin:4px 0 10px}
.compare{display:flex;gap:8px;justify-content:center}
.compare figure{text-align:center;font-size:10px}
.molecule{width:82px;height:110px;border-radius:4px;margin-bottom:4px;background:linear-gradient(160deg,#e9f5fc,#9fcbe8)}
.compare svg{align-self:center}
.result{text-align:center;font-size:12px;margin-top:12px;border:1px solid #bcd4e4;padding:4px 0}
.result strong{display:block;color:var(--accent);font-size:13px}
</style>
</head>
<body>
<main class="page">
  <p class="lead">話題のシリカ水を自社ブランドでつくりませんか？</p>
  <h1 class="title">高濃度シリカ水</h1>
  <p class="lot">小ロット 100 本〜</p>

  <div class="bottles" role="img" aria-label="ペットボトルの水2本と水しぶきの写真"></div>

  <div class="feature f1">科学的に<br>優れた<br>機能水</div>
  <div class="feature f2">シリカ濃度<br>調整可</div>
  <div class="feature f3">非晶質シリカ<br>「水溶性ケイ素 aqsi」<br>配合</div>
  <div class="feature f4">選べる<br>サイズ</div>

  <p class="intro">注目のミネラル「シリカ」とカラダに浸透しやすい機能水をブレンドし<br>独自技術によってナノコロイダル化に成功した高濃度シリカ水</p>

  <section class="card card-silica">
    <div class="card-head"><div class="main">非晶質シリカ</div><div class="sub">水溶性ケイ素 aqsi</div></div>
    <ul class="points">
      <li>機能性、安全性エビデンスの充実（ヒト臨床試験済、非臨床データ）</li>
      <li>アジアハラール認証取得</li>
      <li>シリカは植物由来、鉱物由来の2種タイプから選択可能</li>
    </ul>
  </section>

  <section class="card card-water">
    <p class="tag">科学的に優れた水</p>
    <p class="name">機能水</p>
    <div class="compare">
      <figure><div class="molecule" role="img" aria-label="一般的な水の大きな分子集団の図"></div>（一般的な水）</figure>
      <svg width="14" height="20" viewBox="0 0 14 20"><path d="M2 2 L12 10 L2 18 Z" fill="#2c9be0"/></svg>
      <figure><div class="molecule" role="img" aria-label="生体機能水の微細な分子の図"></div>（生体機能水）</figure>
    </div>
    <p class="result">微細分子＆活発な状態<strong>→浸透性が高い</strong></p>
  </section>
</main>
</body>
</html>
```